Ledgerwise Systems Group business card design.

We are a software development company that develop Software for finance companies and related industries.

We need a 2 sided business card designed. We have a new logo already designed (see attached eps and ai) We are after a clean simple corporate look. One side with just our logo, and the second side with our details.

Mark Hollister
Managing Director

Suite 4 Level 9, 138 Kellaway Street Sydney NSW 2000

Direct: +61 2 9374 6021
Mobile: +61 4 2287 5196
Email: markh@lsg-example.net.au
Web: www.lsg-example.net.au

I have included 2 logo files an .ai and .eps. I noticed that the lines either side of the group looks a bit jaggered and needs to be made sharper.

I would like to introduce a little colour somewhere rather than having it all black and white. But not over the top, keeping with a simple clean corporate look. Perhaps a light blue on some of the text?

If you have other ideas would be pleased to review

Regards

Mark H.

```html
<!DOCTYPE html>
<html lang="en">
<head>
<meta charset="utf-8">
<title>Ledgerwise Systems Group — Business Card</title>
<link rel="stylesheet" href="https://fonts.googleapis.com/css2?family=Michroma&family=Arimo:wght@400;700&family=Open+Sans:wght@400&display=swap">
<style>
  :root {
    --backdrop: #1f1c1b;
    --card-black: #0d0d0e;
    --card-edge: #1a1a1c;
    --silver: #c9c9cb;
    --white: #ffffff;
    --accent-blue: #2f7fd0;
    --muted: #d8d8d8;
  }
  * { margin: 0; padding: 0; box-sizing: border-box; }
  html, body {
    width: 1200px; height: 716px; overflow: hidden;
    background: var(--backdrop);
  }
  .canvas {
    position: relative; width: 1200px; height: 716px;
  }
  .card {
    position: absolute; top: 199px;
    width: 520px; height: 318px;
    background: linear-gradient(160deg, #161617 0%, var(--card-black) 60%);
    border: 1px solid var(--card-edge);
    overflow: hidden;
  }
  .card--front { left: 50px; }
  .card--back { left: 630px; }

  /* Front */
  .brand {
    position: absolute; inset: 0;
    display: flex; flex-direction: column; align-items: center; justify-content: center; gap: 22px;
  }
  .brand__mark {
    width: 58px; height: 58px; background: var(--silver);
  }
  .brand__name {
    font-family: "Michroma", sans-serif;
    font-size: 20px; color: var(--silver);
    letter-spacing: 1px; text-transform: uppercase;
  }

  /* Back */
  .holder {
    position: absolute; right: 28px; top: 44px; text-align: right;
  }
  .holder__name {
    font-family: "Michroma", sans-serif;
    font-size: 19px; color: var(--white);
    letter-spacing: 2px; text-transform: uppercase;
    padding: 0 2px 4px 14px;
    border-bottom: 2px solid var(--accent-blue);
  }
  .holder__title {
    font-family: "Open Sans", sans-serif;
    font-size: 10px; color: var(--muted);
    margin-top: 4px;
  }
  .contact {
    position: absolute; display: flex; align-items: center; gap: 5px;
    font-family: "Arimo", sans-serif; color: var(--white);
    white-space: nowrap;
  }
  .contact svg { width: 12px; height: 12px; flex: none; }
  .contact--direct { left: 18px; top: 96px; font-size: 14px; }
  .contact--email { left: 196px; top: 150px; font-size: 14px; }
  .contact--mobile { left: 326px; top: 196px; font-size: 14px; }
  .contact--web { left: 18px; top: 220px; font-size: 11px; font-weight: 700; }
  .contact--address { left: 190px; top: 236px; font-size: 11.5px; }
  .stripes {
    position: absolute; left: 186px; right: 0; top: 256px;
  }
  .stripes span { display: block; }
  .stripe--white { height: 5px; background: var(--white); }
  .stripe--blue { height: 7px; background: var(--accent-blue); }
  .stripe--gap { height: 3px; }
</style>
</head>
<body>
<main class="canvas">

  <section class="card card--front" aria-label="Card front">
    <div class="brand">
      <div class="brand__mark"></div>
      <div class="brand__name">Ledgerwise Systems Group</div>
    </div>
  </section>

  <section class="card card--back" aria-label="Card back">
    <div class="holder">
      <div class="holder__name">Mark Hollister</div>
      <div class="holder__title">Managing Director</div>
    </div>

    <div class="contact contact--direct">
      <svg viewBox="0 0 12 12"><rect width="12" height="12" fill="#2f7fd0"/><path d="M3.5 2.5h1.5l.6 2-1 .7a5 5 0 0 0 2.2 2.2l.7-1 2 .6v1.5c0 .5-.4.9-.9.9A6.6 6.6 0 0 1 2.6 3.4c0-.5.4-.9.9-.9z" fill="#fff"/></svg>
      <span>+61 2 9374 6021</span>
    </div>

    <div class="contact contact--email">
      <svg viewBox="0 0 12 12"><rect width="12" height="12" fill="#2f7fd0"/><rect x="2.5" y="3.5" width="7" height="5" fill="none" stroke="#fff" stroke-width="1"/><path d="M2.5 3.5 6 6.5l3.5-3" fill="none" stroke="#fff" stroke-width="1"/></svg>
      <span>markh@lsg-example.net.au</span>
    </div>

    <div class="contact contact--mobile">
      <svg viewBox="0 0 12 12"><rect width="12" height="12" fill="#2f7fd0"/><rect x="4" y="2" width="4" height="8" rx="0.8" fill="none" stroke="#fff" stroke-width="1"/><circle cx="6" cy="8.6" r="0.5" fill="#fff"/></svg>
      <span>+61 4 2287 5196</span>
    </div>

    <div class="contact contact--web">
      <svg viewBox="0 0 12 12"><rect width="12" height="12" fill="#2f7fd0"/><circle cx="6" cy="6" r="3.5" fill="none" stroke="#fff" stroke-width="1"/><path d="M2.5 6h7M6 2.5c-1.5 2-1.5 5 0 7M6 2.5c1.5 2 1.5 5 0 7" fill="none" stroke="#fff" stroke-width="0.8"/></svg>
      <span>www.lsg-example.net.au</span>
    </div>

    <div class="contact contact--address">
      <svg viewBox="0 0 12 12"><rect width="12" height="12" fill="#2f7fd0"/><path d="M6 10.2 3.4 6.4A3 3 0 1 1 8.6 6.4z" fill="#fff"/><circle cx="6" cy="4.8" r="1" fill="#2f7fd0"/></svg>
      <span>Suite 4 Level 9, 138 Kellaway Street Sydney NSW 2000</span>
    </div>

    <div class="stripes" aria-hidden="true">
      <span class="stripe--white"></span>
      <span class="stripe--blue"></span>
      <span class="stripe--gap"></span>
      <span class="stripe--white"></span>
      <span class="stripe--blue"></span>
    </div>
  </section>

</main>
</body>
</html>
```